Restaurant menu design

I need a menu for a restaurant in Spain.
It has to be bohemian but modern. We need something romantic and elegant.
The restaurant is elegant with good food and an excellent reputation. It is also modern at the same time.
The restaurant is superbly decorated and very chick so we need something "class" to fit in with the surroundings.
The size of the document must be 325 mm in high and 245 mm as a maximum and preferably made in indesign.

Reason: Thank you all for your designs.
So far all your designs are ok but it isn´t what we are looking for. Most of the designs are too loaded, too many colors and too much decoration.

Target Market(s)

Adults of various age groups and different nationalities mostly European.

Industry/Entity Type

Restaurant

Requirements
Must have
• The menu must have two interior pages with the text as in the document attached.It must be easily legible.
Nice to have
• See what kind of menus they use in important restaurants in places like Paris, see what designs are in trend, but Not necessarily doing the same style if it doesn’t fit in with the description above.
Should not have
• Nothing old fashioned.

```html
<!DOCTYPE html>
<html lang="es">
<head>
<meta charset="UTF-8">
<title>La Violette — Carta</title>
<link rel="stylesheet" href="https://fonts.googleapis.com/css2?family=Parisienne&family=Tinos:ital@1&display=swap">
<style>
  :root {
    --bg: #000000;
    --page: #252527;
    --heading: #a8507f;
    --item: #f2f2f2;
    --price: #c05a8e;
    --figure-top: #4a4a4d;
    --figure-bottom: #2e2e31;
  }
  * { margin: 0; padding: 0; box-sizing: border-box; }
  html, body {
    width: 1200px; height: 791px; overflow: hidden; background: var(--bg);
  }
  .menu-spread {
    position: relative; width: 1200px; height: 791px;
    background: var(--page);
    display: grid;
    grid-template-columns: 1fr 90px 1fr;
    padding: 18px 30px;
    column-gap: 20px;
    overflow: hidden;
  }
  .menu-column { display: flex; flex-direction: column; min-width: 0; }
  .menu-section { display: flex; flex-direction: column; align-items: center; }
  .section-title {
    font-family: "Parisienne", cursive;
    font-weight: 400;
    color: var(--heading);
    font-size: 60px;
    line-height: 1.1;
    align-self: flex-start;
    margin-bottom: 4px;
    white-space: nowrap;
  }
  .section-title.small { font-size: 46px; align-self: center; }
  .section-title.wide { font-size: 46px; align-self: center; }
  .dish-list { list-style: none; text-align: center; }
  .dish {
    font-family: "Tinos", serif;
    font-style: italic;
    color: var(--item);
    font-size: 14px;
    line-height: 19px;
  }
  .price {
    color: var(--price);
    font-size: 10px;
    margin-left: 12px;
    white-space: nowrap;
  }
  .starters { margin-bottom: 20px; }
  .grill { margin-bottom: 16px; }
  .mains { margin-bottom: 12px; }
  .sauces {
    flex-direction: row; align-items: baseline; justify-content: center;
    gap: 16px; margin-bottom: 10px;
  }
  .sauces .section-title { font-size: 32px; align-self: auto; margin: 0; }
  .sauce {
    font-family: "Tinos", serif; font-style: italic; color: var(--item);
    font-size: 12px; white-space: nowrap;
  }
  .sauce .price { font-size: 9px; margin-left: 6px; }
  .dancer-figure {
    align-self: center;
    justify-self: center;
    width: 80px; height: 420px;
  }
</style>
</head>
<body>
<main class="menu-spread">
  <section class="menu-column">
    <div class="menu-section starters">
      <h2 class="section-title">Entradas</h2>
      <ul class="dish-list">
        <li class="dish">Ensalada La Violette. Lechuga, tomate.<span class="price">7,75 €</span></li>
        <li class="dish">Ensalada Caprese (Tomate y Mozzarella).<span class="price">7,75 €</span></li>
        <li class="dish">Escarola al Queso de Cabra con Bacon.<span class="price">6,75 €</span></li>
        <li class="dish">Cocktail de Gambas, Langostinos y Aguacate.<span class="price">7,50 €</span></li>
        <li class="dish">La Sopa de Pescado.<span class="price">8,25 €</span></li>
        <li class="dish">Crema de Espárragos Trigueros y Calabacín.<span class="price">5,95 €</span></li>
        <li class="dish">Carpaccio de Ternera<span class="price">11,50 €</span></li>
        <li class="dish">Carpaccio de Salmón al Eneldo<span class="price">9,75 €</span></li>
        <li class="dish">Carpaccio de Atún<span class="price">13,95 €</span></li>
        <li class="dish">Melón con Jamón Ibérico<span class="price">9,25 €</span></li>
        <li class="dish">Parrillada de Verduras<span class="price">7,95 €</span></li>
        <li class="dish">Parrillada de Verduras Gratinada al Queso de Cabra<span class="price">8,95 €</span></li>
        <li class="dish">Gambas Roja de la Bahía<span class="price">12,95 €</span></li>
      </ul>
    </div>
    <div class="menu-section grill">
      <h2 class="section-title">Pescados al Grill</h2>
      <ul class="dish-list">
        <li class="dish">Lubina al Hinojo<span class="price">15,50 €</span></li>
        <li class="dish">Lubina Fileteada y su Salsa Rústica con Berenjena<span class="price">18,50 €</span></li>
        <li class="dish">Filete de Rodaballo y su Salsa de Marisco<span class="price">17,25 €</span></li>
        <li class="dish">Dorada del Mediterráneo<span class="price">13,95 €</span></li>
        <li class="dish">Lenguado al Grill con Hierbas Provenzales<span class="price">20,75 €</span></li>
        <li class="dish">Pieza de Atún Fresco y su Salsa Griega<span class="price">18,95 €</span></li>
        <li class="dish">Lomo de Salmón con Salsa de Frambuesa<span class="price">11,25 €</span></li>
        <li class="dish">Parrillada de Pescado y Marisco<span class="price">23,50 €</span></li>
      </ul>
    </div>
    <div class="menu-section kids">
      <h2 class="section-title small">Especial Niños</h2>
      <ul class="dish-list">
        <li class="dish">Solomillo Junior, huevo y patatas fritas<span class="price">6,25 €</span></li>
        <li class="dish">Fish &amp; chips<span class="price">6,25 €</span></li>
      </ul>
    </div>
  </section>

  <svg class="dancer-figure" viewBox="0 0 80 420" role="img" aria-label="Slender illustration of a flamenco dancer in a long spotted dress, arm raised">
    <defs>
      <linearGradient id="dancerTone" x1="0" y1="0" x2="0" y2="1">
        <stop offset="0" stop-color="#4a4a4d"/>
        <stop offset="1" stop-color="#2e2e31"/>
      </linearGradient>
    </defs>
    <rect x="0" y="0" width="80" height="420" rx="40" fill="url(#dancerTone)"/>
  </svg>

  <section class="menu-column">
    <div class="menu-section mains">
      <h2 class="section-title">Carnes</h2>
      <ul class="dish-list">
        <li class="dish">Pechuga de Pollo “Belle Rive” con Champiñones y Bacon<span class="price">11,95 €</span></li>
        <li class="dish">Chuletas de Cordero<span class="price">14,50 €</span></li>
        <li class="dish">Costillas de Cerdo con Salsa Barbacoa<span class="price">9,95 €</span></li>
        <li class="dish">Paletilla de Cordero Lechal<span class="price">19,75 €</span></li>
        <li class="dish">Le Strogonoff. Finas tiras de Solomillo con su Salsa de Champiñones<span class="price">15,90 €</span></li>
        <li class="dish">Solomillo de Ternera<span class="price">18,50 €</span></li>
        <li class="dish">Solomillo de Ternera a la Ibérica con Jamón Ibérico y Vino Tinto<span class="price">20,75 €</span></li>
        <li class="dish">“Casa Violeta Steak Haché” Picata de Solomillo, Huevo y Patatas<span class="price">14,50 €</span></li>
        <li class="dish">Solomillo de Cerdo al Horno con Bacon y su Salsa de Setas<span class="price">14,25 €</span></li>
        <li class="dish">Entrecôte de Ternera<span class="price">14,75 €</span></li>
        <li class="dish">T-Bone Steak de Ternera<span class="price">16,75 €</span></li>
        <li class="dish">Chuletón de Ternera<span class="price">20,25 €</span></li>
        <li class="dish">Parrillada de Carnes y Embutidos<span class="price">21,50 €</span></li>
      </ul>
    </div>
    <div class="menu-section sauces">
      <h3 class="section-title">Salsas:</h3>
      <span class="sauce">Pimienta<span class="price">2,85 €</span></span>
      <span class="sauce">Roquefort<span class="price">2,95 €</span></span>
      <span class="sauce">Bearnaise<span class="price">2,95 €</span></span>
      <span class="sauce">de Champiñones<span class="price">2,65 €</span></span>
    </div>
    <div class="menu-section desserts">
      <h2 class="section-title wide">Los Postres de La Violette</h2>
      <ul class="dish-list">
        <li class="dish">Frambuesas “La Violette”<span class="price">6,25 €</span></li>
        <li class="dish">Cocktail de Frutas Exóticas<span class="price">5,25 €</span></li>
        <li class="dish">Sorbete de Limón, Coulis de Fresa y Vodka<span class="price">5,50 €</span></li>
        <li class="dish">Pastel de Chocolate Casero con su Salsa de Vainilla<span class="price">6,25 €</span></li>
        <li class="dish">Crême Brulée<span class="price">6,25 €</span></li>
        <li class="dish">Tarta de Manzana Casera “Tatin” y su Helado de Vainilla<span class="price">6,95 €</span></li>
        <li class="dish">Copa Nevada<span class="price">6,75 €</span></li>
        <li class="dish">Pera al Chocolate Caliente y Helado de Macadamia<span class="price">5,95 €</span></li>
        <li class="dish">Tarta de Queso con Coulis de Fresa<span class="price">5,75 €</span></li>
        <li class="dish">Nuestra Mousse de Chocolate<span class="price">5,75 €</span></li>
      </ul>
    </div>
  </section>
</main>
</body>
</html>
```